Volta Medica Innovative Business Card

Stunning business card. Background will be black. Letters in gold. Modern yet simple design that is attention grabbing. QR code leading to site. Attractive primarily to males ages 30 to 50 but also to females in same age range looking for beauty and mental health products

Target Market(s)

Males in the 30-50 age demographics

Industry/Entity Type

Pharmaceuticals selling erectile dysfunction and mens health medications

Contact Information for Business Card

www.voltamedica.example; (555) NOW-BOLT; info@voltamedica.example

Colors
FFC000
F8CF3A
FAE287
FDF2CF
FEFAEE

Requirements
Must have
• Black business card with gold letters.
Nice to have
• perhaps just the logo or the "R" icon by itself on one side
Should not have
• too much content so it does not look busy

```html
<!DOCTYPE html>
<html lang="en">
<head>
<meta charset="utf-8">
<title>Volta Medica — Business Card</title>
<link href="https://fonts.googleapis.com/css2?family=Montserrat:wght@400;700;800&display=swap" rel="stylesheet">
<style>
  :root {
    --stage: #161616;
    --card: #221f20;
    --card-pattern: #2a2620;
    --gold: #d9b23a;
    --gold-soft: #c9a32f;
  }
  * { box-sizing: border-box; margin: 0; padding: 0; }
  html, body {
    width: 1200px; height: 1000px; overflow: hidden;
    background: var(--stage);
    font-family: "Montserrat", sans-serif;
  }
  .sheet {
    width: 1200px; height: 1000px;
    display: flex; flex-direction: column;
    align-items: center; justify-content: center; gap: 60px;
  }
  .card {
    position: relative;
    width: 700px; height: 400px;
    background: var(--card);
    border-radius: 4px;
    box-shadow: 0 18px 40px rgba(0,0,0,.55);
    overflow: hidden;
  }
  /* Front */
  .contact {
    position: absolute; left: 64px; bottom: 70px;
    color: var(--gold);
  }
  .contact__name {
    font-weight: 800; font-size: 26px; letter-spacing: .5px;
    text-transform: uppercase;
  }
  .contact__role {
    font-size: 17px; margin: 4px 0 26px 18px;
  }
  .contact__list { list-style: none; padding-left: 30px; }
  .contact__item {
    display: flex; align-items: center; gap: 8px;
    font-size: 17px; line-height: 27px;
  }
  .contact__icon { width: 15px; height: 15px; flex: none; fill: var(--gold); }
  .divider {
    position: absolute; left: 400px; top: 110px;
    width: 2px; height: 170px; background: var(--gold);
  }
  .brand {
    position: absolute; display: flex; align-items: center; gap: 12px;
    color: var(--gold); font-weight: 800; text-transform: uppercase;
  }
  .brand__dot { border-radius: 50%; background: var(--gold); flex: none; }
  .card--front .brand { left: 440px; top: 168px; font-size: 26px; line-height: 1.05; }
  .card--front .brand__dot { width: 34px; height: 34px; }
  /* Back */
  .pattern {
    position: absolute; inset: 0;
    background: linear-gradient(135deg, var(--card-pattern), #1f1c1b 70%);
  }
  .card--back .brand { right: 56px; top: 150px; font-size: 28px; line-height: 1.05; }
  .card--back .brand__dot { width: 38px; height: 38px; }
</style>
</head>
<body>
<main class="sheet">

  <section class="card card--front" aria-label="Business card front">
    <div class="contact">
      <p class="contact__name">Marcus Hale</p>
      <p class="contact__role">Founder</p>
      <ul class="contact__list">
        <li class="contact__item">
          <svg class="contact__icon" viewBox="0 0 16 16"><path d="M3 1h3l1 4-2 1a9 9 0 0 0 5 5l1-2 4 1v3a2 2 0 0 1-2 2A13 13 0 0 1 1 3a2 2 0 0 1 2-2z"/></svg>
          (555) NOW-BOLT
        </li>
        <li class="contact__item">
          <svg class="contact__icon" viewBox="0 0 16 16"><path d="M1 3h14v10H1z M1 3l7 6 7-6" fill="none" stroke="currentColor" stroke-width="1.6" style="stroke:var(--gold)"/></svg>
          info@voltamedica.example
        </li>
        <li class="contact__item">
          <svg class="contact__icon" viewBox="0 0 16 16"><circle cx="8" cy="8" r="7" fill="none" stroke-width="1.5" style="stroke:var(--gold)"/><path d="M1 8h14M8 1c-3 4-3 10 0 14M8 1c3 4 3 10 0 14" fill="none" stroke-width="1.2" style="stroke:var(--gold)"/></svg>
          www.voltamedica.example
        </li>
      </ul>
    </div>
    <div class="divider"></div>
    <div class="brand">
      <span class="brand__dot"></span>
      <span class="brand__name">Volta<br>Medica</span>
    </div>
  </section>

  <section class="card card--back" aria-label="Business card back">
    <div class="pattern" role="img" aria-label="Faint repeating brand monogram pattern in dark gold across the card"></div>
    <div class="brand">
      <span class="brand__dot"></span>
      <span class="brand__name">Volta<br>Medica</span>
    </div>
  </section>

</main>
</body>
</html>
```